Sticker label for natural moisturizer

I need a sticker label designed for a homemade moisturizer made from beef tallow and honey.
Must include: Logo, product name (Classic Suet & Clover Salve), ingredients (in English and Polish, can use placeholder text for initial design), brief description of product with instructions for use (in English and Polish, can use placeholder text for initial design), manufacturer name (vorelmart.com), manufacturer address (placeholder text for initial design), volume of container (60ml / 2oz)
The product is used by both males and females of all ages, so must be unisex design with broad appeal.
Dimensions: Length 15cm, Height 3cm
Style: Has to simultaneously communicate that this is a homemade product with no chemical fillers AND that it is of extremely high quality.
Brand colors:
#57665C
#FCFAF6
#FFFFFF
#000000
#B99B83
#EAE4DD
#CC8E5A

```html
<!DOCTYPE html>
<html lang="en">
<head>
<meta charset="utf-8">
<title>Classic Suet &amp; Clover Salve – Sticker Label</title>
<link href="https://fonts.googleapis.com/css2?family=Poppins:wght@400&family=Oswald:wght@500;600&family=Playfair+Display:wght@500&display=swap" rel="stylesheet">
<style>
  :root {
    --sage: #57665C;
    --paper: #FCFAF6;
    --white: #FFFFFF;
    --ink: #000000;
    --taupe: #B99B83;
    --linen: #EAE4DD;
    --copper: #CC8E5A;
    --page: #FDFDFD;
  }
  * { margin: 0; padding: 0; box-sizing: border-box; }
  html, body {
    width: 1200px; height: 1200px; overflow: hidden;
    background: var(--page);
  }
  .canvas { position: relative; width: 1200px; height: 1200px; }

  .label {
    position: absolute; left: 84px; top: 492px;
    width: 1037px; height: 207px;
    background: var(--linen);
    font-family: "Poppins", sans-serif;
    color: var(--copper);
  }
  .label > * { position: absolute; }

  .guide-h { height: 1px; background: var(--ink); }
  .guide-v { width: 1px; background: var(--ink); }

  .section-title {
    font-size: 15px; font-weight: 400; line-height: 1; text-align: center; white-space: nowrap;
    transform: translateX(-50%);
  }
  .section-body {
    font-size: 12px; font-weight: 400; line-height: 14.8px; text-align: justify;
  }
  .section-body.wide { font-size: 14px; line-height: 17.6px; }
  .maker-address { font-size: 10px; line-height: 1; transform: translateX(-50%); white-space: nowrap; }

  .art {
    border-radius: 50% 40% 55% 45%;
  }
  .art-left {
    left: 226px; top: 17px; width: 125px; height: 175px;
    background: radial-gradient(ellipse at 60% 40%, rgba(87,102,92,0.85), rgba(204,142,90,0.6) 60%, rgba(185,155,131,0) 100%);
  }
  .art-right {
    left: 677px; top: 2px; width: 152px; height: 190px;
    background: radial-gradient(ellipse at 45% 35%, rgba(204,142,90,0.8), rgba(87,102,92,0.75) 55%, rgba(87,102,92,0) 100%);
  }

  .brand-frame {
    left: 371px; top: 36px; width: 287px; height: 135px;
    border: 2.5px solid var(--copper);
  }
  .brand-frame .divider { position: absolute; background: var(--copper); }
  .brand-frame .divider-logo { left: 50px; top: 0; bottom: 0; width: 2.5px; }
  .brand-frame .divider-info { left: 50px; right: 0; top: 93px; height: 2.5px; }
  .brand-frame .divider-volume { left: 183px; top: 93px; bottom: 0; width: 2.5px; }

  .brand-name {
    position: absolute; left: 25px; top: 65px;
    transform: translate(-50%, -50%) rotate(-90deg);
    font-family: "Playfair Display", serif; font-weight: 500;
    font-size: 44px; line-height: 1; color: var(--ink); white-space: nowrap;
  }

  .product-name {
    position: absolute; left: 62px; top: 14px;
    font-family: "Oswald", sans-serif; font-weight: 600; color: var(--copper);
    text-transform: uppercase; white-space: nowrap;
  }
  .product-name .line-one { display: block; font-size: 27px; line-height: 33px; letter-spacing: 0; }
  .product-name .line-two { display: block; font-size: 27px; line-height: 33px; letter-spacing: 1.5px; }
  .ampersand {
    position: absolute; left: 244px; top: 14px;
    font-family: "Oswald", sans-serif; font-weight: 600; font-size: 56px; line-height: 1;
    color: var(--copper);
  }
  .site, .volume {
    position: absolute; top: 103px;
    font-family: "Oswald", sans-serif; font-weight: 500; font-size: 18px; line-height: 20px;
    color: var(--copper); text-transform: uppercase; white-space: nowrap;
  }
  .site { left: 62px; }
  .volume { left: 196px; }
</style>
</head>
<body>
<div class="canvas">
  <section class="label">
    <div class="guide-h" style="left:-2px; top:104px; width:315px;"></div>
    <div class="guide-v" style="left:284px; top:17px; height:173px;"></div>

    <h2 class="section-title" style="left:144px; top:19px;">product with instructions</h2>
    <p class="section-body" style="left:14px; top:44px; width:255px;">Lorem ipsum dolor sit amet, consectetuer adipiscing elit, sed diam nonummy nibh euismod</p>
    <h2 class="section-title" style="left:141px; top:108px;">produkt z instrukcją</h2>
    <p class="section-body" style="left:15px; top:128px; width:255px;">Lorem ipsum dolor sit amet, consectetuer adipiscing elit, sed diam nonummy nibh euismod</p>
    <p class="maker-address" style="left:138px; top:182px;">manufacturer address</p>

    <div class="art art-left" role="img" aria-label="Botanical illustration of copper and sage leaves"></div>

    <div class="brand-frame">
      <span class="divider divider-logo"></span>
      <span class="divider divider-info"></span>
      <span class="divider divider-volume"></span>
      <span class="brand-name">vorel</span>
      <h1 class="product-name">
        <span class="line-one">Classic Suet</span>
        <span class="line-two">Clover Salve</span>
      </h1>
      <span class="ampersand">&amp;</span>
      <span class="site">vorelmart.com</span>
      <span class="volume">60ml / 2oz</span>
    </div>

    <div class="art art-right" role="img" aria-label="Botanical illustration of a sage leaf, copper leaf and scattered seeds"></div>

    <div class="guide-h" style="left:721px; top:104px; width:316px;"></div>
    <div class="guide-v" style="left:767px; top:17px; height:173px;"></div>

    <h2 class="section-title" style="left:908px; top:21px;">ingredients</h2>
    <p class="section-body wide" style="left:783px; top:42px; width:238px;">Lorem ipsum dolor sit amet, consectetuer adipiscing elit, sed diam nonummy nibh euismod</p>
    <h2 class="section-title" style="left:903px; top:111px;">składniki</h2>
    <p class="section-body wide" style="left:784px; top:130px; width:238px;">Lorem ipsum dolor sit amet, consectetuer adipiscing elit, sed diam nonummy nibh euismod</p>
  </section>
</div>
</body>
</html>
```